PW Law Firm Needs Sharp Letterhead

Our law firm recently selected a new logo through Pitchgrove. Now we need a sharp Letterhead using the Letterhead.

Target Market(s)

Legal community, business clients

Industry/Entity Type

Law Firm

Requirements
Must have
• Our Logo
• Gerald P. Hollis
• Board Certified
• Civil Trial Law
• Harrow Council of Courtroom Accreditation
• ghollis@pwadvocates.net
• 2715-C West Larkin
• McAllen, TX 78504
• 956-555-0182
• www.pwadvocates.net

```html
<!DOCTYPE html>
<html lang="en">
<head>
<meta charset="utf-8">
<title>Pryce Whitlock Letterhead</title>
<link rel="stylesheet" href="https://fonts.googleapis.com/css2?family=Cinzel:wght@400;500&family=Tinos&display=swap">
<style>
  :root {
    --paper: #ffffff;
    --ink: #1a1a1a;
    --mid-grey: #8a8a8a;
    --soft-grey: #9a9a9a;
    --pale-grey: #cfcfcf;
    --stone-light: #f2f2f2;
    --stone-dark: #bdbdbd;
  }
  * { margin: 0; padding: 0; box-sizing: border-box; }
  html, body { width: 848px; height: 1200px; overflow: hidden; background: var(--paper); }
  .letterhead { position: relative; width: 848px; height: 1200px; background: var(--paper); }

  .header-photo {
    position: absolute; left: 0; top: 0; width: 314px; height: 157px;
    background: linear-gradient(90deg, var(--stone-light) 0%, #dcdcdc 40%, var(--stone-dark) 75%, #e6e6e6 100%);
  }
  .header-band {
    position: absolute; left: 314px; top: 133px; width: 534px; height: 14px;
    background: var(--mid-grey);
  }
  .header-band__url {
    position: absolute; right: 8px; top: 0; line-height: 14px;
    font-family: "Tinos", serif; font-size: 11px; color: var(--paper);
  }

  .brand { position: absolute; left: 359px; top: 40px; }
  .brand__square {
    position: absolute; left: 0; top: 0; width: 54px; height: 54px;
    background: var(--ink);
  }
  .brand__name {
    position: absolute; left: 69px; top: -4px; width: 380px;
    font-family: "Cinzel", serif; font-weight: 500; font-size: 37px;
    letter-spacing: 1px; color: var(--ink); white-space: nowrap; line-height: 42px;
    padding-bottom: 1px; border-bottom: 1px solid var(--soft-grey);
  }
  .brand__tagline {
    position: absolute; left: 69px; top: 44px; width: 380px;
    font-family: "Cinzel", serif; font-weight: 400; font-size: 15px;
    letter-spacing: 1.5px; color: var(--mid-grey); white-space: nowrap;
  }

  .corner-block {
    position: absolute; left: 652px; top: 975px; width: 172px; height: 158px;
    background: var(--pale-grey);
  }

  .footer { position: absolute; left: 0; top: 1140px; width: 848px; text-align: center;
    font-family: "Tinos", serif; color: var(--ink); white-space: nowrap; }
  .footer__attorney { font-size: 12px; line-height: 18px; color: var(--mid-grey); }
  .footer__contact { font-size: 13.5px; line-height: 20px; margin-top: 2px; }
  .footer__dot {
    display: inline-block; width: 5px; height: 5px; border-radius: 50%;
    background: var(--soft-grey); margin: 0 6px; vertical-align: middle;
  }
</style>
</head>
<body>
  <div class="letterhead">
    <div class="header-photo" role="img" aria-label="Photograph of classical stone columns in a row"></div>
    <div class="header-band"><span class="header-band__url">www.pwadvocates.net</span></div>

    <div class="brand">
      <div class="brand__square"></div>
      <div class="brand__name">Pryce Whitlock</div>
      <div class="brand__tagline">Attorneys and Counselors</div>
    </div>

    <div class="corner-block"></div>

    <footer class="footer">
      <p class="footer__attorney">Gerald P. Hollis<span class="footer__dot"></span>Board Certified, Civil Trial Law<span class="footer__dot"></span>Harrow Council of Courtroom Accreditation</p>
      <p class="footer__contact">2715-C West Larkin, McAllen, TX&nbsp; 78504<span class="footer__dot"></span>956-555-0182<span class="footer__dot"></span>ghollis@pwadvocates.net<span class="footer__dot"></span>www.pwadvocates.net</p>
    </footer>
  </div>
</body>
</html>
```